VerdaloMD is an aesthetics and wellness medical spa. I am looking for a modern site, not too glam, not too boring. Currently I have the coming soon page at verdaloMD.com. The green in the logo is the accent color. I need the site to be semi neutral. I don't want it to be too geared towards females because there are some consults that men also will participate in.

```html
<!DOCTYPE html>
<html lang="en">
<head>
<meta charset="utf-8">
<title>VerdaloMD – Aesthetics and Wellness Medical Spa</title>
<link href="https://fonts.googleapis.com/css2?family=Poppins:wght@400;500;600;700&family=Great+Vibes&display=swap" rel="stylesheet">
<style>
:root{
  --sage:#b9d6cb;
  --sage-deep:#9fc4b6;
  --ink:#111417;
  --text:#4a4f52;
  --muted:#8a8f92;
  --white:#ffffff;
  --mist:#f3f3f3;
}
*{box-sizing:border-box;margin:0;padding:0}
html,body{width:1200px;height:3665px;overflow:hidden}
body{font-family:"Poppins",sans-serif;color:var(--ink);background:var(--white);position:relative}
.abs{position:absolute}
.script{font-family:"Great Vibes",cursive;font-weight:400}

/* top bar + nav */
.topbar{left:0;top:0;width:1200px;height:28px;background:var(--sage);font-size:10px;color:var(--ink)}
.topbar span{position:absolute;top:8px}
.navbar{left:0;top:28px;width:1200px;height:74px;background:var(--white);z-index:3}
.brand-pill{left:111px;top:11px;width:235px;height:103px;background:var(--white);border-radius:50px;z-index:4;display:flex;align-items:center;justify-content:center}
.brand{font-size:27px;font-weight:500;color:var(--ink);letter-spacing:.2px}
.nav a{position:absolute;top:56px;font-size:12px;color:#555;text-decoration:none;z-index:4}
.btn-contact{left:979px;top:46px;width:111px;height:36px;border-radius:18px;background:var(--sage);font-size:12px;font-weight:600;display:flex;align-items:center;justify-content:center;z-index:4}

/* hero */
.hero-visual{left:0;top:102px;width:1200px;height:680px;background:linear-gradient(100deg,#2a3326 0%,#3f4a36 35%,#8b6a52 62%,#5a4a3c 82%,#2e3a2b 100%)}
.hero-script{left:130px;top:290px;font-size:44px;color:var(--white);white-space:nowrap}
.hero-title{left:129px;top:338px;font-size:50px;font-weight:700;color:var(--sage);letter-spacing:.5px}
.hero-copy{left:130px;top:410px;width:440px;font-size:12.5px;line-height:22px;color:var(--white)}
.btn-register{left:130px;top:477px;width:109px;height:35px;border:1.5px solid var(--white);border-radius:18px;color:var(--white);font-size:12px;font-weight:600;display:flex;align-items:center;justify-content:center}

/* about */
.about-visual{left:0;top:700px;width:460px;height:530px;background:radial-gradient(ellipse at 30% 45%,#c9b7a5 0%,#9fae8e 38%,rgba(233,237,229,.8) 68%,rgba(255,255,255,0) 88%)}
.about-title{left:501px;top:848px;font-size:42px;font-weight:600;white-space:nowrap}
.about-title .script{font-size:48px;margin-left:12px}
.about-copy{left:501px;top:925px;width:555px;font-size:12px;line-height:21px;color:var(--text)}
.about-copy p+p{margin-top:20px}
.btn-view{left:502px;top:1076px;width:110px;height:36px;border-radius:18px;background:var(--sage);font-size:12px;font-weight:600;display:flex;align-items:center;justify-content:center}

/* services */
.services-band{left:0;top:1230px;width:1200px;height:546px;background:var(--sage)}
.services-visual{left:230px;top:1150px;width:720px;height:626px;background:radial-gradient(ellipse at 50% 45%,rgba(150,120,105,.28) 0%,rgba(185,214,203,0) 70%)}
.services-title{left:0;top:1272px;width:1200px;text-align:center;font-size:44px;font-weight:600}
.services-title .script{font-size:48px;margin-right:12px}
.service{width:270px;text-align:center}
.service .icon{display:block;margin:0 auto;height:88px}
.service h3{font-size:15px;font-weight:500;margin-top:14px}
.service p{font-size:12px;line-height:20px;color:#2d3234;margin-top:18px}
.service.lower .icon{height:70px}
.center-mark{left:559px;top:1482px;width:82px;height:82px;border:2px solid var(--ink);border-radius:50%}

/* blog */
.section-title{left:0;width:1200px;text-align:center;font-size:42px;font-weight:600;white-space:nowrap}
.section-title .script{font-size:48px;margin-left:12px}
.section-copy{left:0;width:1200px;text-align:center;font-size:12px;line-height:21px;color:var(--text)}
.post{width:272px;height:334px;background:var(--white);border-radius:6px;box-shadow:0 8px 24px rgba(0,0,0,.12);overflow:hidden}
.post.featured{background:var(--sage)}
.post-visual{width:100%;height:172px}
.post h4{position:absolute;left:26px;top:210px;font-size:14.5px;font-weight:500}
.post .rule{position:absolute;left:26px;top:236px;width:36px;height:2px;background:var(--sage)}
.post.featured .rule{background:var(--ink)}
.post p{position:absolute;left:26px;top:252px;width:215px;font-size:12px;line-height:21px;color:var(--text)}
.post.featured p{color:#2d3234}
.post svg.arrow{position:absolute;right:22px;top:312px}

/* signup */
.signup-band{left:0;top:2545px;width:1200px;height:612px;background:var(--mist)}
.field{height:50px;border-radius:25px;background:var(--white);box-shadow:0 3px 8px rgba(0,0,0,.12);font-size:12px;color:var(--muted);padding:0 26px;display:flex;align-items:center}
.btn-signup{left:400px;top:3002px;width:400px;height:50px;border-radius:25px;background:var(--sage);font-size:12px;font-weight:600;display:flex;align-items:center;justify-content:center}

/* footer */
.footer{left:0;top:3157px;width:1200px;height:508px;background:var(--sage)}
.footer-brand{left:101px;top:3236px;font-size:29px;font-weight:500}
.footer-copy{left:101px;top:3316px;width:280px;font-size:12px;line-height:25.5px;color:var(--ink)}
.social{top:3421px;width:29px;height:29px;border-radius:50%;background:var(--ink)}
.footer-heading{position:absolute;top:3233px;font-size:21px;font-weight:500}
.contact-row{left:535px;font-size:12px;line-height:25.5px;color:var(--ink)}
.contact-icon{left:497px}
.pages a{position:absolute;left:931px;font-size:12px;color:var(--ink);text-decoration:none}
.footer-rule{left:111px;top:3559px;width:978px;height:1px;background:rgba(0,0,0,.25)}
.copyright{left:0;top:3604px;width:1200px;text-align:center;font-size:12px;color:var(--ink)}
</style>
</head>
<body>

<!-- top bar -->
<div class="abs topbar">
  <svg class="abs" style="left:694px;top:6px" width="16" height="16" viewBox="0 0 16 16" fill="none" stroke="#111" stroke-width="1.2"><path d="M3 2 l3 0 1 4-2 1 c1 2 2 3 4 4 l1-2 4 1 0 3 c-6 1-12-5-11-11z"/></svg>
  <span style="left:721px">P: 555 018 2046</span>
  <svg class="abs" style="left:836px;top:4px" width="16" height="18" viewBox="0 0 16 18" fill="none" stroke="#111" stroke-width="1.2"><path d="M8 17 C3 11 2 9 2 7 a6 6 0 0 1 12 0 c0 2-1 4-6 10z"/><circle cx="8" cy="7" r="2.2"/></svg>
  <span style="left:858px">18 Fernbrook Lane, Mossvale, ACT, 2990</span>
</div>

<!-- navigation -->
<div class="abs navbar"></div>
<div class="abs brand-pill"><span class="brand">VerdaloMD.</span></div>
<nav class="nav">
  <a style="left:540px">Home</a>
  <a style="left:617px">About Us</a>
  <a style="left:706px">Services</a>
  <a style="left:793px">FAQ</a>
  <a style="left:864px">Testimonials</a>
</nav>
<div class="abs btn-contact">Contact Us</div>

<!-- hero -->
<div class="abs hero-visual" role="img" aria-label="Smiling woman in a straw hat outdoors among greenery"></div>
<div class="abs hero-script script">Aesthetics and Wellness</div>
<div class="abs hero-title">Medical Spa</div>
<p class="abs hero-copy">Contrary to popular belief, Lorem Ipsum is not simply random text. It has roots in a piece of classical Latin literature from</p>
<div class="abs btn-register">Register</div>

<svg class="abs" style="left:0;top:640px" width="1200" height="150" viewBox="0 0 1200 150">
  <path d="M0 95 C80 80 170 80 240 82 C360 86 440 55 520 45 C600 35 640 130 720 122 C800 114 830 20 900 18 C980 16 1050 70 1200 70 L1200 150 L0 150 Z" fill="#b9d6cb"/>
  <path d="M0 108 C80 92 170 92 240 94 C360 98 440 72 520 62 C600 52 640 145 720 136 C800 127 830 40 900 38 C980 36 1060 92 1200 88 L1200 150 L0 150 Z" fill="#ffffff"/>
</svg>

<!-- about -->
<div class="abs about-visual" role="img" aria-label="Woman stretching her arms upward beside a leafy plant"></div>
<h2 class="abs about-title">Look And Feel<span class="script">Your Best</span></h2>
<div class="abs about-copy">
  <p>From Smooth-skin parties (we can come to you), dermal fillers, IV therapy, ED, BHRT, Peptides, Personal training to mental health services and Opiate use help – These services and more, Coming soon.</p>
  <p>Start or continue your aesthetics and Wellness journey here. Find out about The latest procedures, the do's and dont's, what works and what doesn't.</p>
</div>
<div class="abs btn-view">View More</div>

<!-- services -->
<svg class="abs" style="left:0;top:1135px" width="1200" height="110" viewBox="0 0 1200 110">
  <path d="M0 105 L0 110 L1200 110 L1200 70 C1120 60 1060 10 960 12 C860 14 800 55 720 60 C620 66 560 100 500 96 C430 92 400 20 330 10 C250 0 200 50 120 70 C60 85 20 95 0 105 Z" fill="#b9d6cb"/>
</svg>
<div class="abs services-band"></div>
<div class="abs services-visual" role="img" aria-label="Faint portrait of a bearded man"></div>
<h2 class="abs services-title"><span class="script">Our</span>Services</h2>

<div class="abs service" style="left:245px;top:1322px">
  <div class="icon"><svg width="60" height="88" viewBox="0 0 60 88" fill="none" stroke="#111" stroke-width="1.6"><circle cx="30" cy="48" r="22"/><path d="M30 36 c-6 8-8 11-8 14 a8 8 0 0 0 16 0 c0-3-2-6-8-14z"/></svg></div>
  <h3>Smooth-skin parties</h3>
  <p>Contrary to popular belief, Lorem Ipsum<br>is not simply random text.</p>
</div>
<div class="abs service" style="left:676px;top:1322px">
  <div class="icon"><svg width="60" height="88" viewBox="0 0 60 88" fill="none" stroke="#111" stroke-width="1.6"><circle cx="30" cy="48" r="22"/><path d="M30 36 v24 M18 48 h24"/></svg></div>
  <h3>Dermal fillers</h3>
  <p>Contrary to popular belief, Lorem Ipsum<br>is not simply random text.</p>
</div>
<div class="abs service lower" style="left:245px;top:1544px">
  <div class="icon"><svg width="60" height="70" viewBox="0 0 60 70" fill="none" stroke="#111" stroke-width="1.6"><circle cx="30" cy="36" r="22"/><path d="M21 36 l6 6 12-12"/></svg></div>
  <h3>Peptides</h3>
  <p>Contrary to popular belief, Lorem Ipsum<br>is not simply random text.</p>
</div>
<div class="abs service lower" style="left:676px;top:1544px">
  <div class="icon"><svg width="60" height="70" viewBox="0 0 60 70" fill="none" stroke="#111" stroke-width="1.6"><circle cx="30" cy="36" r="22"/><path d="M30 46 c-10-6-12-10-12-13 a5 5 0 0 1 12-2 a5 5 0 0 1 12 2 c0 3-2 7-12 13z"/></svg></div>
  <h3>Mental Health</h3>
  <p>Contrary to popular belief, Lorem Ipsum<br>is not simply random text.</p>
</div>
<div class="abs center-mark"></div>

<!-- blog -->
<h2 class="abs section-title" style="top:1885px">What's New<span class="script">From Blog</span></h2>
<p class="abs section-copy" style="top:1966px">From Smooth-skin parties (we can come to you), dermal fillers, IV therapy, ED, BHRT, Peptides,<br>Personal training to mental health services and Opiate use help -</p>

<article class="abs post" style="left:158px;top:2060px">
  <div class="post-visual" role="img" aria-label="Woman with purple orchids near her face" style="background:linear-gradient(120deg,#7a2a78,#c9a08e 60%,#e8cbb8)"></div>
  <h4>Aesthetics and Wellness</h4><div class="rule"></div>
  <p>Contrary to popular belief, Lorem Ipsum is not simply</p>
  <svg class="arrow" width="14" height="10" viewBox="0 0 14 10" fill="none" stroke="#888" stroke-width="1.2"><path d="M1 5 h11 M8 1 l4 4-4 4"/></svg>
</article>
<article class="abs post featured" style="left:462px;top:2060px">
  <div class="post-visual" role="img" aria-label="Smiling man wearing sunglasses" style="background:linear-gradient(120deg,#1d1d1d,#6b4a3a 55%,#2a2a2a)"></div>
  <h4>Latest Procedures</h4><div class="rule"></div>
  <p>Contrary to popular belief, Lorem Ipsum is not simply</p>
  <svg class="arrow" width="14" height="10" viewBox="0 0 14 10" fill="none" stroke="#111" stroke-width="1.8"><path d="M1 5 h11 M8 1 l4 4-4 4"/></svg>
</article>
<article class="abs post" style="left:764px;top:2060px">
  <div class="post-visual" role="img" aria-label="Woman with auburn hair and red lipstick" style="background:linear-gradient(120deg,#6b4a36,#d8b39c 55%,#8a5a3e)"></div>
  <h4>Aesthetics and Wellness</h4><div class="rule"></div>
  <p>Contrary to popular belief, Lorem Ipsum is not simply</p>
  <svg class="arrow" width="14" height="10" viewBox="0 0 14 10" fill="none" stroke="#888" stroke-width="1.2"><path d="M1 5 h11 M8 1 l4 4-4 4"/></svg>
</article>

<!-- signup -->
<div class="abs signup-band"></div>
<svg class="abs" style="left:0;top:2480px" width="1200" height="140" viewBox="0 0 1200 140">
  <path d="M0 70 C90 60 180 20 290 10 C400 0 440 40 520 70 C600 100 650 40 760 50 C880 60 980 110 1200 100 L1200 140 L0 140 Z" fill="#b9d6cb"/>
  <path d="M0 90 C90 80 180 40 290 30 C400 20 440 60 520 90 C600 120 650 62 760 72 C880 82 980 124 1200 118 L1200 140 L0 140 Z" fill="#f3f3f3"/>
</svg>
<h2 class="abs section-title" style="top:2666px">Sign up for our<span class="script">Upcoming Launch</span></h2>
<p class="abs section-copy" style="top:2749px">From Smooth-skin parties (we can come to you), dermal fillers, IV therapy, ED, BHRT, Peptides,<br>Personal training to mental health services and Opiate use help -</p>
<div class="abs field" style="left:310px;top:2837px;width:277px">Name</div>
<div class="abs field" style="left:611px;top:2837px;width:277px">Email*</div>
<div class="abs field" style="left:312px;top:2911px;width:578px">Phone*</div>
<div class="abs btn-signup">Sign Up</div>

<!-- footer -->
<footer class="abs footer"></footer>
<div class="abs footer-brand">VerdaloMD.</div>
<p class="abs footer-copy">Lorem ipsum dolor sit amet, consectetur adipisicing elit, sed do eiusmod tempor incididunt ut labore et dolore</p>
<div class="abs social" style="left:105px"></div>
<div class="abs social" style="left:145px"></div>
<div class="abs social" style="left:184px"></div>
<div class="abs social" style="left:223px"></div>

<h5 class="footer-heading" style="left:497px">Contact</h5>
<svg class="abs contact-icon" style="top:3318px" width="16" height="18" viewBox="0 0 16 18" fill="none" stroke="#111" stroke-width="1.2"><path d="M8 17 C3 11 2 9 2 7 a6 6 0 0 1 12 0 c0 2-1 4-6 10z"/><circle cx="8" cy="7" r="2.2"/></svg>
<p class="abs contact-row" style="top:3314px">Address:<br>214 Linden Crest Road #12, Alderton,<br>ST 40512, United States</p>
<svg class="abs contact-icon" style="top:3421px" width="16" height="16" viewBox="0 0 16 16" fill="none" stroke="#111" stroke-width="1.2"><path d="M3 2 l3 0 1 4-2 1 c1 2 2 3 4 4 l1-2 4 1 0 3 c-6 1-12-5-11-11z"/></svg>
<p class="abs contact-row" style="top:3416px">Phone: +1 555-014-2270</p>
<svg class="abs contact-icon" style="top:3447px" width="16" height="16" viewBox="0 0 16 16" fill="none" stroke="#111" stroke-width="1.2"><rect x="4" y="1.5" width="8" height="4"/><rect x="1.5" y="5.5" width="13" height="6" rx="1"/><rect x="4" y="9.5" width="8" height="5"/></svg>
<p class="abs contact-row" style="top:3442px">Fax: +1 555-014-2271</p>
<svg class="abs contact-icon" style="top:3473px" width="16" height="14" viewBox="0 0 16 14" fill="none" stroke="#111" stroke-width="1.2"><rect x="1" y="2" width="14" height="10"/><path d="M1 2 l7 6 7-6"/></svg>
<p class="abs contact-row" style="top:3467px">Email: hello@verdaloMD.com</p>
<svg class="abs contact-icon" style="top:3498px" width="16" height="16" viewBox="0 0 16 16" fill="none" stroke="#111" stroke-width="1.2"><circle cx="8" cy="8" r="6.5"/><ellipse cx="8" cy="8" rx="3" ry="6.5"/><path d="M1.5 8 h13"/></svg>
<p class="abs contact-row" style="top:3493px">Website: verdaloMD.com</p>

<h5 class="footer-heading" style="left:931px">Pages</h5>
<nav class="pages">
  <a style="top:3324px">Home</a>
  <a style="top:3355px">About Us</a>
  <a style="top:3386px">Services</a>
  <a style="top:3417px">FAQ</a>
  <a style="top:3448px">Testimonials</a>
</nav>
<div class="abs footer-rule"></div>
<p class="abs copyright">© 2020-22 VerdaloMD &nbsp;|&nbsp; Terms of Use &nbsp;|&nbsp; Membership Terms &amp; Conditions &nbsp;|&nbsp; Privacy Policy</p>

</body>
</html>
```